Newsletter Banner Ad with a URL to our website offering

We need a banner ad for a newsletter that is published to members biweekly that simply articulates our value proposition and enables the reader to click on our logo to learn more and engage with us to schedule an Emergency Response Plan so they are ready for when a burst pipe happens on their property. They will have a plan after they engage with us.
We need quotes to build two options 1&2

```html
<!DOCTYPE html>
<html lang="en">
<head>
<meta charset="utf-8">
<title>Newsletter Banner Options</title>
<link href="https://fonts.googleapis.com/css2?family=Bebas+Neue&family=Arimo:wght@700&family=Oswald:wght@700&display=swap" rel="stylesheet">
<style>
  :root {
    --page: #ffffff;
    --red: #d0000b;
    --red-bright: #e8202a;
    --blue: #0a1fa8;
    --navy: #05079a;
    --white: #ffffff;
    --ink: #111111;
  }
  * { margin: 0; padding: 0; box-sizing: border-box; }
  html, body { width: 1200px; height: 1000px; overflow: hidden; background: var(--page); }
  .canvas { position: relative; width: 1200px; height: 1000px; }
  .banner {
    position: absolute; left: 179px; width: 841px; height: 218px; overflow: hidden;
    box-shadow: 0 1px 3px rgba(0,0,0,0.25);
  }
  .banner--option-one { top: 215px; }
  .banner--option-two { top: 567px; }
  .banner svg { position: absolute; inset: 0; }
  .brand {
    position: absolute; display: flex; align-items: center; gap: 7px;
    font-family: "Oswald", sans-serif; font-weight: 700; color: var(--ink);
    font-size: 15px; line-height: 1.05; letter-spacing: 0.5px; text-transform: uppercase;
  }
  .brand__dot { width: 14px; height: 14px; border-radius: 50%; background: var(--red); flex: none; }
  .banner--option-one .brand { left: 270px; top: 78px; width: 150px; }
  .banner--option-two .brand { left: 30px; top: 86px; width: 150px; }
  .headline-caps {
    position: absolute; left: 532px; top: 36px;
    font-family: "Bebas Neue", sans-serif; color: var(--white);
    font-size: 55px; line-height: 52px; letter-spacing: 0.3px;
  }
  .headline-mixed {
    position: absolute; left: 451px; top: 50px;
    font-family: "Arimo", sans-serif; font-weight: 700; color: var(--white);
    letter-spacing: -0.3px;
  }
  .headline-mixed__lead { display: block; font-size: 45px; line-height: 50px; }
  .headline-mixed__rest { display: block; font-size: 31px; line-height: 43px; }
</style>
</head>
<body>
<main class="canvas">

  <section class="banner banner--option-one">
    <svg width="841" height="218" viewBox="0 0 841 218">
      <defs>
        <linearGradient id="spray-tone" x1="0" y1="0" x2="1" y2="0">
          <stop offset="0" stop-color="#a9a49e"/>
          <stop offset="0.3" stop-color="#d9d6d2"/>
          <stop offset="0.6" stop-color="#f4f3f2"/>
          <stop offset="1" stop-color="#ffffff"/>
        </linearGradient>
      </defs>
      <rect width="841" height="218" fill="var(--page)"/>
      <rect width="420" height="218" fill="url(#spray-tone)" role="img" aria-label="Photo of a burst red pipe spraying water"/>
      <ellipse cx="760" cy="109" rx="302" ry="300" fill="var(--blue)"/>
      <ellipse cx="660" cy="109" rx="176" ry="166" fill="var(--red)"/>
    </svg>
    <div class="brand"><span class="brand__dot"></span>Ridgeway Property Restoration</div>
    <h2 class="headline-caps">Do you have a<br>rapid response<br>plan for this?</h2>
  </section>

  <section class="banner banner--option-two">
    <svg width="841" height="218" viewBox="0 0 841 218">
      <defs>
        <linearGradient id="hall-tone" x1="0" y1="0" x2="0" y2="1">
          <stop offset="0" stop-color="#d8ccc0"/>
          <stop offset="0.55" stop-color="#c9b8a8"/>
          <stop offset="1" stop-color="#8a4f30"/>
        </linearGradient>
      </defs>
      <rect width="460" height="218" fill="url(#hall-tone)" role="img" aria-label="Photo of a flooded building hallway"/>
      <path d="M385 0 Q455 109 378 218 L841 218 L841 0 Z" fill="var(--red-bright)"/>
      <path d="M412 0 Q470 109 386 218 L841 218 L841 0 Z" fill="var(--navy)"/>
    </svg>
    <div class="brand"><span class="brand__dot"></span>Ridgeway Property Restoration</div>
    <h2 class="headline-mixed">
      <span class="headline-mixed__lead">Do you have a</span>
      <span class="headline-mixed__rest">rapid response</span>
      <span class="headline-mixed__rest">plan for this?</span>
    </h2>
  </section>

</main>
</body>
</html>
```